Business Stationery
Business card, letter head and compliment slip
Professional
Jake Hollins
Managing Director
Four Larkmead Row
Birmingham
B7 4QN
jake@corvastel.org.uk
corvastel.org.uk
Corvastel is an appointed representative of Pelvarin Ltd which is authorised and regulated by the Market Conduct Tribunal.

```html
<!DOCTYPE html>
<html lang="en">
<head>
<meta charset="utf-8">
<title>Corvastel Business Stationery</title>
<link rel="stylesheet" href="https://fonts.googleapis.com/css2?family=Arimo:wght@400;700&family=Pinyon+Script&display=swap">
<style>
  :root {
    --paper: #ffffff;
    --ink: #1b1b1b;
    --brand-red: #d0111b;
    --strip-dark: #2d2d2d;
    --strip-text: #8a8a8a;
    --panel-dark: #262626;
    --panel-mid: #4a4a4a;
    --faint: #eeeeee;
    --muted: #555555;
    --edge: #d8d8d8;
  }
  * { box-sizing: border-box; margin: 0; padding: 0; }
  html, body { width: 1200px; height: 914px; overflow: hidden; background: var(--paper); }
  body { position: relative; font-family: "Arimo", Arial, sans-serif; color: var(--ink); }

  .sheet {
    position: absolute; background: var(--paper);
    border: 1px solid var(--edge);
    box-shadow: 3px 4px 8px rgba(0,0,0,0.18);
    overflow: hidden;
  }

  /* Brand name lock-up */
  .brand { position: absolute; display: flex; flex-direction: column; }
  .brand-row { display: flex; align-items: center; gap: 6px; }
  .brand-mark { width: 14px; height: 14px; background: var(--brand-red); }
  .brand-name { font-weight: 700; color: var(--ink); letter-spacing: -0.5px; line-height: 1; }
  .brand-tagline { font-size: 10px; color: var(--ink); margin-top: 2px; }

  .brand-faint {
    position: absolute; font-weight: 700; color: var(--faint);
    letter-spacing: -2px; line-height: 1; white-space: nowrap;
  }

  .side-strip {
    position: absolute; left: 0; top: 0; bottom: 0;
    background: linear-gradient(90deg, var(--strip-dark), #454545);
    display: flex; align-items: center; justify-content: center;
  }
  .side-strip span {
    writing-mode: vertical-rl; transform: rotate(180deg);
    color: var(--strip-text); font-size: 12px; white-space: nowrap;
  }

  .web { position: absolute; color: var(--brand-red); font-weight: 700; }

  /* Business card front */
  .card-front { left: 67px; top: 36px; width: 475px; height: 276px; }
  .card-front .panel {
    position: absolute; left: 216px; top: 0; right: 0; bottom: 0;
    background: linear-gradient(90deg, var(--panel-dark), var(--panel-mid) 70%, #3a3a3a);
  }
  .card-front .band { position: absolute; top: 0; bottom: 0; background: var(--brand-red); }
  .card-front .details { position: absolute; left: 293px; top: 22px; text-align: center; width: 160px; color: #e8e8e8; }
  .card-front .name { color: var(--brand-red); font-size: 21px; }
  .card-front .role { font-size: 10px; color: #cfcfcf; margin-top: 2px; }
  .card-front .address { font-size: 10px; line-height: 1.5; margin-top: 30px; }
  .card-front .contacts { position: absolute; left: 300px; top: 192px; font-size: 10px; line-height: 1.45; color: #e8e8e8; list-style: none; }
  .card-front .contacts b { color: var(--brand-red); margin-right: 6px; }

  /* Business card back */
  .card-back { left: 67px; top: 340px; width: 475px; height: 170px; }

  /* Compliment slip */
  .slip { left: 67px; top: 557px; width: 902px; height: 322px; }
  .slip .greeting { position: absolute; left: 172px; top: 140px; display: flex; align-items: center; }
  .slip .greeting em { font-family: "Pinyon Script", cursive; font-style: normal; font-size: 22px; color: var(--ink); }
  .slip .greeting i { display: block; width: 340px; height: 1px; background: var(--ink); margin-left: 6px; }
  .slip .contacts { position: absolute; left: 53px; top: 198px; list-style: none; font-size: 14px; line-height: 1.5; }
  .slip .contacts b { color: var(--brand-red); display: inline-block; width: 22px; }

  /* Letterhead */
  .letterhead { left: 571px; top: 43px; width: 557px; height: 756px; }
  .letterhead .name { position: absolute; left: 408px; top: 78px; color: var(--brand-red); font-size: 15px; }
  .letterhead .role { position: absolute; left: 408px; top: 98px; font-size: 8px; color: var(--muted); }
  .letterhead .footer { position: absolute; left: 30px; right: 0; top: 665px; text-align: center; font-size: 11px; line-height: 1.6; }
  .letterhead .footer b { color: var(--brand-red); margin: 0 3px 0 8px; }
</style>
</head>
<body>

<section class="sheet card-front" aria-label="Business card front">
  <div class="brand-faint" style="left:22px; top:168px; font-size:80px;">corvastel</div>
  <div class="brand" style="left:50px; top:40px;">
    <div class="brand-row"><span class="brand-mark"></span><span class="brand-name" style="font-size:30px;">corvastel</span></div>
    <span class="brand-tagline" style="font-size:8px;">Independent financial advice for Doctors</span>
  </div>
  <div class="web" style="left:52px; top:252px; font-size:10px;">corvastel.org.uk</div>
  <div class="panel"></div>
  <div class="band" style="left:216px; width:12px;"></div>
  <div class="band" style="left:234px; width:6px;"></div>
  <div class="details">
    <div class="name">Jake Hollins</div>
    <div class="role">Managing Director</div>
    <div class="address">Four Larkmead Row<br>Birmingham<br>B7 4QN</div>
  </div>
  <ul class="contacts">
    <li><b>P</b>0121 4960183</li>
    <li><b>C</b>07700 900415</li>
    <li><b>F</b>0121 496 0772</li>
    <li><b>E</b>jake@corvastel.org.uk</li>
  </ul>
</section>

<section class="sheet card-back" aria-label="Business card back">
  <div class="side-strip" style="width:28px;"><span style="font-size:9px;">Independent financial advice for Doctors</span></div>
  <div class="brand-faint" style="left:34px; top:108px; font-size:72px;">corvastel</div>
  <div class="brand" style="left:178px; top:36px;">
    <div class="brand-row"><span class="brand-mark"></span><span class="brand-name" style="font-size:30px;">corvastel</span></div>
    <span class="brand-tagline" style="font-size:8px;">Independent financial advice for Doctors</span>
  </div>
  <div class="web" style="left:230px; top:100px; font-size:13px;">corvastel.org.uk</div>
</section>

<section class="sheet slip" aria-label="Compliment slip">
  <div class="side-strip" style="width:34px;"><span>Independent financial advice for Doctors</span></div>
  <div class="brand" style="left:53px; top:28px;">
    <div class="brand-row"><span class="brand-mark"></span><span class="brand-name" style="font-size:34px;">corvastel</span></div>
    <span class="brand-tagline">Independent financial advice for Doctors</span>
  </div>
  <div class="greeting"><em>With Best Compliment</em><i></i></div>
  <ul class="contacts">
    <li><b>P</b>0121 4960183</li>
    <li><b>C</b>07700 900415</li>
    <li><b>F</b>0121 496 0772</li>
    <li><b>E</b>jake@corvastel.org.uk</li>
  </ul>
  <div class="web" style="left:735px; top:288px; font-size:14px;">corvastel.org.uk</div>
</section>

<section class="sheet letterhead" aria-label="Letterhead">
  <div class="side-strip" style="width:30px;"><span>Independent financial advice for Doctors</span></div>
  <div class="brand" style="left:52px; top:56px;">
    <div class="brand-row"><span class="brand-mark"></span><span class="brand-name" style="font-size:36px;">corvastel</span></div>
    <span class="brand-tagline">Independent financial advice for Doctors</span>
  </div>
  <div class="name">Jake Hollins</div>
  <div class="role">Managing Director</div>
  <div class="footer">
    <div><b>P</b>0121 4960183 <b>C</b>07700 900415 <b>F</b>0121 496 0772</div>
    <div><b>E</b>jake@corvastel.org.uk <b>W</b>corvastel.org.uk</div>
  </div>
</section>

</body>
</html>
```